BRKL informational brochure to aimed to attract people to all three our our service industries

This brochure is designed to be multi purposed, here are a few objectives:
1. To provide a receipt for septic services rendered onsite to customers. The receipt has coupons to entice each customer to use us in the future. This brochure also gives this customer tips on how to best keep their septic system from developing issues. By providing additional company information the septic customer can become educated about the other lines of service we provide in the area, i.e. Trash pick up, & roll-off dumpsters. Optimally we would want a septic customer to be so impressed with our septic work that they would trust us to serve them in the other areas we offer.
2. The brochure is a means of obtaining ratings and reviews for our online profiles, i.e. Zentrix, & Marla's roster. It is already hard enough to get a customer to give us 5-star ratings, so this is a useful tool to try and bait the customer to get a price reduction on their total cost for septic services by rating us or performing an online review. We want to have a place on the brochure that references our current 5-star ratings on Zentrix, Pinwheel, and Marla's roster see the attached example.
3. This brochure is not only useful for septic clients but can also be used for general advertising, we leave these brochures in a variety of public locations. Thus it would be efficient to show all lines of business and provide the information needed to acquire new clients.
4. Photographs are a critical component of our plan, customers like to SEE what we do and who we are. Thus, please find a creative way of including photos of what we offer by means of services and products. For individuals who have seen our brand around town, a photographic reminder might help this potential clients to recognizing who we are.
5. I will attach a copy of our last ArtGather project to this project to give you an idea of how we like to present ourselves.
6. We want to encourage the Spanish speaking individuals to call us for translated material.
7. We need to mention pricing on this brochure for all 3 lines of business, i'll find a way to provide those to you.
8. We don't know what size to choose, one size is 8.5'' x 11'' the other size is 8.5'' x 14'. Perhaps you can help us choose. not sure if we should have a trifold (3 pane) or quadfold (4 pane) brochure. We want to express ourselves creatively and not just provide boring information.
9. we need to have an american flag somewhere on display
Target Market(s)
Rural areas of North Texas, Our office is in Ponder TX and we serve 35 mile radius.
Industry/Entity Type
Waste Management

```html
<!DOCTYPE html>
<html lang="en">
<head>
<meta charset="utf-8">
<title>Brazos Ridge Waste &amp; Septic Solutions – Trifold Brochure</title>
<link rel="stylesheet" href="https://fonts.googleapis.com/css2?family=Lato:wght@400;700;900&family=Oswald:wght@600&family=Libre+Baskerville:wght@400;700&family=Montserrat:wght@800&display=swap">
<style>
  :root{
    --ink:#0b0b0b;
    --gold:#f5c518;
    --white:#ffffff;
    --paper:#e6e6e6;
    --form-field:#d9d9d9;
    --coupon:#e9e9e9;
    --red:#c8102e;
    --muted:#cfcfcf;
  }
  *{box-sizing:border-box;margin:0;padding:0}
  html,body{width:1200px;height:800px;overflow:hidden;background:var(--paper)}
  body{font-family:"Lato",sans-serif;color:var(--white);position:relative}
  .brochure{position:absolute;left:45px;top:20px;width:1110px;height:760px;background:var(--ink);overflow:hidden;box-shadow:0 6px 24px rgba(0,0,0,.25)}
  .band{position:absolute;inset:0}
  .abs{position:absolute}

  /* review row */
  .reviews{left:28px;top:70px;display:flex;gap:22px;align-items:flex-end}
  .review{display:flex;flex-direction:column;align-items:flex-start;gap:3px}
  .review-name{display:flex;align-items:center;gap:6px;font-weight:700;font-size:17px;color:var(--white)}
  .review-name .dot{width:12px;height:12px;background:var(--gold);border-radius:50%}
  .stars{color:var(--gold);font-size:12px;letter-spacing:2px}
  .emergency{left:250px;top:128px;text-align:center;line-height:1;transform:rotate(-8deg)}
  .emergency .big{font-family:"Montserrat",sans-serif;font-size:34px;font-weight:800}
  .emergency .small{font-size:12px;font-weight:900;font-style:italic}

  /* form */
  .habla{left:28px;top:270px;font-family:"Libre Baskerville",serif;font-weight:700;font-size:19px;color:var(--red);line-height:1.05}
  .overview{left:36px;top:330px;width:230px;height:220px;background:var(--white);border:3px solid var(--ink);padding:14px 14px;color:var(--ink)}
  .overview h3{font-size:15px;font-weight:700;text-align:center;line-height:1.15;margin-bottom:10px}
  .field{font-size:11px;background:var(--form-field);padding:4px 6px;margin-bottom:5px}
  .field.tall{height:58px}
  .person{left:250px;top:380px;width:110px;height:190px;border-radius:40px 40px 6px 6px;background:linear-gradient(#d8e2ee,#8ea4c0)}

  /* contact */
  .contact{left:36px;top:600px}
  .contact h2{font-family:"Montserrat",sans-serif;font-size:36px;font-weight:800;line-height:.95}
  .contact h2 span{color:var(--gold)}
  .phone{font-size:27px;font-weight:700;margin-top:10px}
  .email{font-size:13px;margin-top:3px}
  .web{font-family:"Libre Baskerville",serif;font-size:16px;font-weight:700;color:var(--gold);margin-top:10px}
  .socials{left:290px;top:605px;display:grid;grid-template-columns:repeat(2,22px);gap:10px 12px}
  .socials i{width:22px;height:22px;border:1.5px solid var(--white);border-radius:50%}

  /* middle panel */
  .section-title{font-size:15px;font-weight:700;letter-spacing:.5px;padding-bottom:6px;border-bottom:1.5px solid var(--white);width:300px}
  .body-copy{font-size:11.5px;line-height:1.55;margin-top:8px;color:var(--muted);width:300px}
  .who{left:405px;top:72px}
  .vision{left:405px;top:598px}
  .coupon{background:var(--coupon);border:2px dashed var(--ink);color:var(--ink);text-align:center;padding:8px 12px 10px}
  .coupon .deal{font-family:"Oswald",sans-serif;font-weight:600;font-size:52px;line-height:1;color:var(--gold);-webkit-text-stroke:1px var(--ink)}
  .coupon p{font-size:11px;line-height:1.3;margin-top:4px}
  .coupon-rating{left:420px;top:285px;width:250px}
  .coupon-reminder{left:450px;top:415px;width:260px}

  /* right panel */
  .brand{left:760px;top:40px;display:flex;gap:14px;align-items:flex-start}
  .brand-name{font-family:"Libre Baskerville",serif;font-size:22px;color:var(--gold);line-height:1.2}
  .brand-dot{width:46px;height:46px;border-radius:50%;background:var(--gold);margin-top:4px}
  .years{left:985px;top:450px;width:62px;height:62px;border-radius:50%;background:var(--white)}
  .slogan{left:800px;top:528px;font-family:"Libre Baskerville",serif;font-size:16px;color:var(--gold);text-align:right;width:280px;line-height:1.3}
  .story{left:800px;top:590px;width:280px;font-size:11.5px;text-align:right;line-height:1.5;color:var(--muted);border-top:1.5px solid var(--white);padding-top:8px}
</style>
</head>
<body>
<main class="brochure">
  <svg class="band" viewBox="0 0 1110 760" width="1110" height="760" aria-hidden="false">
    <defs>
      <clipPath id="band-clip">
        <path d="M0,245 L300,245 C340,245 345,215 385,212 L700,192 C745,189 760,168 805,166 L1110,166 L1110,455 L960,460 C920,462 910,500 870,505 L640,552 C600,560 590,540 560,544 L400,560 C360,564 350,595 310,595 L0,595 Z"/>
      </clipPath>
      <linearGradient id="yard" x1="0" y1="0" x2="0" y2="1">
        <stop offset="0" stop-color="#9fc3e2"/><stop offset=".35" stop-color="#e0b52a"/><stop offset="1" stop-color="#6b5a2c"/>
      </linearGradient>
      <linearGradient id="site" x1="0" y1="0" x2="0" y2="1">
        <stop offset="0" stop-color="#3f4a3f"/><stop offset=".5" stop-color="#b8aa8a"/><stop offset="1" stop-color="#d8d2c2"/>
      </linearGradient>
      <linearGradient id="truck" x1="0" y1="0" x2="0" y2="1">
        <stop offset="0" stop-color="#a9c8e8"/><stop offset=".35" stop-color="#2a2a22"/><stop offset=".7" stop-color="#3c6b3a"/><stop offset="1" stop-color="#1c1c1c"/>
      </linearGradient>
    </defs>
    <g clip-path="url(#band-clip)">
      <rect role="img" aria-label="Photo of a yellow roll-off dumpster under a blue sky" x="0" y="150" width="370" height="460" fill="url(#yard)"/>
      <rect role="img" aria-label="Photo of dumpsters on a gravel work site" x="370" y="150" width="370" height="460" fill="url(#site)"/>
      <rect role="img" aria-label="Photo of the septic pumping truck with an American flag flying above it" x="740" y="150" width="370" height="460" fill="url(#truck)"/>
    </g>
    <path d="M0,245 L300,245 C340,245 345,215 385,212 L700,192 C745,189 760,168 805,166 L1110,166" fill="none" stroke="var(--gold)" stroke-width="10"/>
    <path d="M1110,455 L960,460 C920,462 910,500 870,505 L640,552 C600,560 590,540 560,544 L400,560 C360,564 350,595 310,595 L0,595" fill="none" stroke="var(--gold)" stroke-width="10"/>
    <path d="M0,752 L1110,752" stroke="var(--gold)" stroke-width="6"/>
  </svg>

  <!-- left panel -->
  <div class="abs reviews">
    <div class="review"><span class="review-name"><i class="dot"></i>Zentrix</span><span class="stars">★★★★★</span></div>
    <div class="review"><span class="review-name"><i class="dot"></i>Marla's roster</span><span class="stars">★★★★★</span></div>
    <div class="review"><span class="review-name"><i class="dot"></i>Pinwheel</span><span class="stars">★★★★★</span></div>
  </div>
  <div class="abs emergency"><div class="big">24/7</div><div class="small">Emergency<br>Services<br>Available</div></div>

  <div class="abs habla">Se Habla<br>Español</div>
  <section class="abs overview">
    <h3>SEPTIC SERVICE<br>OVERVIEW</h3>
    <div class="field">Today's Date:</div>
    <div class="field">Next Service Date:</div>
    <div class="field">System Type:</div>
    <div class="field"># of Gallons:</div>
    <div class="field tall">Recommendations:</div>
  </section>
  <div class="abs person" role="img" aria-label="Photo of a smiling service representative giving two thumbs up"></div>

  <section class="abs contact">
    <h2>GET IN<br><span>TOUCH:</span></h2>
    <div class="phone">940-555-0142</div>
    <div class="email">brazosridgewaste@inboxly.com</div>
    <div class="email">brazosridgeseptic@inboxly.com</div>
    <div class="web">www.brazosridgewaste.com</div>
  </section>
  <div class="abs socials"><i></i><i></i><i></i><i></i><i></i><i></i></div>

  <!-- middle panel -->
  <section class="abs who">
    <h2 class="section-title">WHO WE ARE</h2>
    <p class="body-copy">BRKL is dedicated to the future growth and development of the local community that graciously hosts our family. Our vision is to be an environmentally friendly company seeking to protect our roads from damage and the air from emissions.</p>
  </section>
  <div class="abs coupon coupon-rating">
    <div class="deal">10% OFF</div>
    <p>Give us a 5 star rating on Zentrix or Marla's roster for $10 off today's cleaning services.</p>
  </div>
  <div class="abs coupon coupon-reminder">
    <div class="deal">$25 OFF</div>
    <p>Save this Septic Reminder<br>for $25 off your next pumping!</p>
  </div>
  <section class="abs vision">
    <h2 class="section-title">OUR VISION</h2>
    <p class="body-copy">To fully express our value of every customer's trust by means of operating under the utmost integrity, while also providing world class service. To grow in size and heart, yet never to outgrow a small-town experience.</p>
  </section>

  <!-- right panel -->
  <div class="abs brand">
    <div class="brand-name">Brazos Ridge<br>Waste &amp; Septic<br>Solutions</div>
    <i class="brand-dot"></i>
  </div>
  <div class="abs years"></div>
  <p class="abs slogan">We don't talk trash,<br>We talk solutions</p>
  <p class="abs story">Brazos Ridge Waste Solutions is a family owned and operated business that started with one truck and a dream...</p>
</main>
</body>
</html>
```